Hochwertiges Etiketten-Design für edle Destillate
Zielgruppe
Wir sind ein Familiengeführter Brennereibetrieb wo wir edle Destillate (Obstbrände und Liköre) herstellen.
Aufgabenstellung
Wir suchen ein hochwertiges Etikett welches eine sofortige Wiedererkennung hat. Unser jetziges Etikett soll als Vorlage gelten, jedoch einiges aufgewertet werden. Unser Logo und und die Farbe Rot soll auf jeden Fall darin vorkommen.
Dies sind unsere verwendeten Flaschen
https://www.vandoro.com/kelm-flasche-500ml-weissglas-mdg.-gpi-28-karton-50stk.html?cPath=5_6
https://www.vandoro.com/kelm-flasche-200ml-weissglas-mdg.-gpi-28-karton-45stk.html?cPath=5_6
https://www.vandoro.com/urma-500-ml-weissglas-mdg.-gpi-28-karton-46stk.html?cPath=5_6
https://www.vandoro.com/urma-200ml-weissglas-mdg.-gpi-28-karton-90stk.html?cPath=5_6
das Design soll skalierbar und auf andere Größen anwendbar sein
Folgende Angaben müssen auf dem Etikett sein (austauschbar):
-Sorte: z.B. Williams
-Produkt: zB. Birnenbrand
-Losnummer: z.B. K3F57382
-Inhalt: z.B. 500ml
-Alkoholgehalt: 40% vol
-Adresse

```html
<!DOCTYPE html>
<html lang="de">
<head>
<meta charset="utf-8">
<title>Harlacher Edelbrände – Etiketten</title>
<link rel="stylesheet" href="https://fonts.googleapis.com/css2?family=Playfair+Display:wght@400;500&family=Oswald:wght@300;400;500&family=Mrs+Saint+Delafield&display=swap">
<style>
  :root {
    --page: #ffffff;
    --slate-dark: #0b0c0e;
    --slate-mid: #24272c;
    --slate-light: #3a3e45;
    --brand-red: #e30613;
    --ornament-red: #8e1a20;
    --ink-light: #f2f2f2;
    --ink-soft: #d9d9d9;
    --rule: #e6e6e6;
  }
  * { box-sizing: border-box; margin: 0; padding: 0; }
  html, body { width: 698px; height: 1200px; overflow: hidden; background: var(--page); }
  .board {
    position: absolute;
    left: 18px; top: 210px;
    display: grid;
    grid-template-columns: repeat(3, 183px);
    grid-auto-rows: 360px;
    column-gap: 56px;
    row-gap: 60px;
  }
  .label {
    position: relative;
    width: 183px; height: 360px;
    color: var(--ink-light);
    text-align: center;
    overflow: hidden;
  }
  .label-texture {
    position: absolute; inset: 0;
    background:
      radial-gradient(ellipse 80% 45% at 50% 42%, var(--slate-light) 0%, var(--slate-mid) 45%, transparent 80%),
      linear-gradient(180deg, var(--slate-dark) 0%, var(--slate-mid) 40%, var(--slate-dark) 100%);
  }
  .label > *:not(.label-texture) { position: absolute; left: 0; right: 0; }
  .brand-tab {
    left: 61px !important; right: auto !important;
    top: 0; width: 61px; height: 45px;
    background: var(--brand-red);
    font-family: "Playfair Display", serif;
    font-size: 6.5px; letter-spacing: 0.4px;
    display: flex; align-items: flex-end; justify-content: center;
    padding-bottom: 4px;
  }
  .house-name {
    top: 50px;
    font-family: "Playfair Display", serif;
    font-size: 10px; letter-spacing: 1.6px;
  }
  .region {
    top: 80px;
    font-family: "Oswald", sans-serif; font-weight: 300;
    font-size: 8px; letter-spacing: 0.8px;
  }
  .variety-script {
    top: 92px;
    font-family: "Mrs Saint Delafield", cursive;
    font-size: 46px; line-height: 70px;
  }
  .variety-script.tall { font-size: 54px; top: 86px; }
  .region-serif {
    top: 94px;
    font-family: "Playfair Display", serif;
    font-size: 6px; letter-spacing: 0.6px;
  }
  .region-serif.large { top: 91px; font-size: 11px; letter-spacing: 2px; }
  .variety-serif {
    top: 103px;
    font-family: "Playfair Display", serif; font-weight: 400;
    font-size: 28px; line-height: 36px;
    font-variant: small-caps; letter-spacing: 1px;
  }
  .variety-serif.wide { font-size: 32px; top: 102px; }
  .product {
    top: 163px;
    font-family: "Oswald", sans-serif; font-weight: 500;
    font-size: 8.5px; line-height: 11px; letter-spacing: 1.2px;
  }
  .product .spaced { letter-spacing: 6px; margin-right: -6px; }
  .ornament {
    position: absolute; top: 166px;
    width: 18px; height: 6px;
    background: var(--ornament-red);
    border-radius: 3px;
  }
  .ornament.left { left: 30px !important; right: auto !important; }
  .ornament.right { right: 30px !important; left: auto !important; }
  .facts {
    left: 16px !important; right: auto !important;
    top: 217px; width: 153px;
    border: 0.8px solid var(--rule);
    display: grid;
    grid-template-columns: 66px 1fr;
    grid-template-rows: 38px 41px 32px;
  }
  .facts > div { border-color: var(--rule); border-style: solid; border-width: 0; }
  .maker {
    grid-row: 1 / 3;
    border-right-width: 0.8px !important;
    display: flex; flex-direction: column; align-items: center; justify-content: center; gap: 3px;
    font-family: "Oswald", sans-serif;
  }
  .maker-mark { width: 16px; height: 16px; border-radius: 50%; background: var(--brand-red); }
  .maker-name { font-size: 8px; font-weight: 500; }
  .maker-sub { font-size: 4.5px; font-weight: 300; color: var(--ink-soft); }
  .volume, .strength {
    font-family: "Oswald", sans-serif; font-weight: 500;
    font-size: 16px; letter-spacing: 0.8px;
    display: flex; align-items: center; justify-content: center;
  }
  .volume { border-bottom-width: 0.8px !important; }
  .address {
    grid-column: 1 / 3;
    border-top-width: 0.8px !important;
    font-family: "Oswald", sans-serif; font-weight: 300;
    font-size: 6.3px; line-height: 10px;
    display: flex; flex-direction: column; justify-content: center;
  }
  .lot {
    left: 16px !important; right: auto !important;
    top: 330px; width: 153px; height: 13px;
    border: 0.8px solid var(--rule);
    font-family: "Oswald", sans-serif; font-weight: 300;
    font-size: 6.3px; line-height: 11px;
  }
</style>
</head>
<body>
<main class="board">

  <!-- Script series -->
  <article class="label">
    <div class="label-texture" role="img" aria-label="Dunkle Schiefer-Textur"></div>
    <div class="brand-tab">HARLACHER</div>
    <div class="house-name">EDELBRÄNDE</div>
    <div class="region">OBERÖSTERREICHISCHE</div>
    <div class="variety-script">Weinbirne</div>
    <span class="ornament left" role="img" aria-label="Rote Zierornamente"></span>
    <div class="product"><span class="spaced">BRAND</span></div>
    <span class="ornament right" role="img" aria-label="Rote Zierornamente"></span>
    <div class="facts">
      <div class="maker"><span class="maker-mark"></span><span class="maker-name">Harlacher</span><span class="maker-sub">Edeldestillerie</span></div>
      <div class="volume">500 ML ℮</div>
      <div class="strength">40% VOL.</div>
      <div class="address"><span>Harlacher Edelbrände</span><span>Lindenweg 7 · 79999 Talheim - Oberau</span></div>
    </div>
    <div class="lot">Losnummer K3F57382</div>
  </article>

  <article class="label">
    <div class="label-texture" role="img" aria-label="Dunkle Schiefer-Textur"></div>
    <div class="brand-tab">HARLACHER</div>
    <div class="house-name">EDELBRÄNDE</div>
    <div class="variety-script">Türkenkirsche</div>
    <span class="ornament left" role="img" aria-label="Rote Zierornamente"></span>
    <div class="product">WILDPFLAUMEN<br><span class="spaced">BRAND</span></div>
    <span class="ornament right" role="img" aria-label="Rote Zierornamente"></span>
    <div class="facts">
      <div class="maker"><span class="maker-mark"></span><span class="maker-name">Harlacher</span><span class="maker-sub">Edeldestillerie</span></div>
      <div class="volume">500 ML ℮</div>
      <div class="strength">40% VOL.</div>
      <div class="address"><span>Harlacher Edelbrände</span><span>Lindenweg 7 · 79999 Talheim - Oberau</span></div>
    </div>
    <div class="lot">Losnummer K3F57382</div>
  </article>

  <article class="label">
    <div class="label-texture" role="img" aria-label="Dunkle Schiefer-Textur"></div>
    <div class="brand-tab">HARLACHER</div>
    <div class="house-name">EDELBRÄNDE</div>
    <div class="region">SCHWARZWÄLDER</div>
    <div class="variety-script tall">Kirsch</div>
    <div class="facts">
      <div class="maker"><span class="maker-mark"></span><span class="maker-name">Harlacher</span><span class="maker-sub">Edeldestillerie</span></div>
      <div class="volume">500 ML ℮</div>
      <div class="strength">40% VOL.</div>
      <div class="address"><span>Harlacher Edelbrände</span><span>Lindenweg 7 · 79999 Talheim - Oberau</span></div>
    </div>
    <div class="lot">Losnummer K3F57382</div>
  </article>

  <!-- Serif series -->
  <article class="label">
    <div class="label-texture" role="img" aria-label="Dunkle Schiefer-Textur"></div>
    <div class="brand-tab">HARLACHER</div>
    <div class="house-name">EDELBRÄNDE</div>
    <div class="region-serif">OBERÖSTERREICHISCHE</div>
    <div class="variety-serif">Weinbirne</div>
    <span class="ornament left" role="img" aria-label="Rote Zierornamente"></span>
    <div class="product"><span class="spaced">BRAND</span></div>
    <span class="ornament right" role="img" aria-label="Rote Zierornamente"></span>
    <div class="facts">
      <div class="maker"><span class="maker-mark"></span><span class="maker-name">Harlacher</span><span class="maker-sub">Edeldestillerie</span></div>
      <div class="volume">500 ML ℮</div>
      <div class="strength">40% VOL.</div>
      <div class="address"><span>Harlacher Edelbrände</span><span>Lindenweg 7 · 79999 Talheim - Oberau</span></div>
    </div>
    <div class="lot">Losnummer K3F57382</div>
  </article>

  <article class="label">
    <div class="label-texture" role="img" aria-label="Dunkle Schiefer-Textur"></div>
    <div class="brand-tab">HARLACHER</div>
    <div class="house-name">EDELBRÄNDE</div>
    <div class="region-serif large">TÜRKEN</div>
    <div class="variety-serif wide">Kirsche</div>
    <span class="ornament left" role="img" aria-label="Rote Zierornamente"></span>
    <div class="product">WILDPFLAUMEN<br><span class="spaced">BRAND</span></div>
    <span class="ornament right" role="img" aria-label="Rote Zierornamente"></span>
    <div class="facts">
      <div class="maker"><span class="maker-mark"></span><span class="maker-name">Harlacher</span><span class="maker-sub">Edeldestillerie</span></div>
      <div class="volume">500 ML ℮</div>
      <div class="strength">40% VOL.</div>
      <div class="address"><span>Harlacher Edelbrände</span><span>Lindenweg 7 · 79999 Talheim - Oberau</span></div>
    </div>
    <div class="lot">Losnummer K3F57382</div>
  </article>

  <article class="label">
    <div class="label-texture" role="img" aria-label="Dunkle Schiefer-Textur"></div>
    <div class="brand-tab">HARLACHER</div>
    <div class="house-name">EDELBRÄNDE</div>
    <div class="region-serif">SCHWARZWÄLDER</div>
    <div class="variety-serif wide">Kirsch</div>
    <span class="ornament left" role="img" aria-label="Rote Zierornamente"></span>
    <div class="product"><span class="spaced">BRAND</span></div>
    <span class="ornament right" role="img" aria-label="Rote Zierornamente"></span>
    <div class="facts">
      <div class="maker"><span class="maker-mark"></span><span class="maker-name">Harlacher</span><span class="maker-sub">Edeldestillerie</span></div>
      <div class="volume">500 ML ℮</div>
      <div class="strength">40% VOL.</div>
      <div class="address"><span>Harlacher Edelbrände</span><span>Lindenweg 7 · 79999 Talheim - Oberau</span></div>
    </div>
    <div class="lot">Losnummer K3F57382</div>
  </article>

</main>
</body>
</html>
```